Hargrove Summit Business Letterhead

Looking for professional letterhead for luxury real estate sales.
Would like main color to be black, waivey like on top, with silver/gray/white accent. I like job #3942297. KEY/STONE Ballon on top left, company name on top right, "Hargrove Summit Properties, KEY/STONE Heritage" Contact information on the bottom of letter. 281-555-0193 summit@dalewynnteam.example. Samples of a logo in progress are included however I am hoping to have the logo changed to black/white rather than full color blue/red. I would prefer the word "Summit" be written with a different font. I also included a generic photo of what our yard signs will look like so you can see the basic color/theme I am going for.

Target Market(s)

High end luxury home buyer/sellers. $500k+, multi million $

Industry/Entity Type

Business

Font styles to use
Serif
Script

Colors
1b1b1b
757575
e8e8e8
c8c8c8
0455a3
ec1f27

Requirements
Must have
• KEYSTONE Balloon - prefer in shiny blue/red if possible. Company name and contact info, PROFESSIONAL yet stylish and modern. Black base color

```html
<!DOCTYPE html>
<html lang="en">
<head>
<meta charset="utf-8">
<title>Hargrove Summit Business Letterhead</title>
<link rel="stylesheet" href="https://fonts.googleapis.com/css2?family=Cormorant+Garamond:wght@500&family=Montserrat:wght@400&display=swap">
<style>
  :root {
    --ink: #1b1b1b;
    --black: #000000;
    --paper: #ffffff;
    --silver-dark: #757575;
    --silver: #c8c8c8;
    --silver-light: #e8e8e8;
  }
  html, body {
    margin: 0;
    padding: 0;
    overflow: hidden;
    background: var(--paper);
  }
  .letterhead {
    position: relative;
    width: 927px;
    height: 1200px;
    overflow: hidden;
    background: var(--paper);
  }
  .header-band, .footer-band {
    position: absolute;
    left: 0;
    width: 927px;
    display: block;
  }
  .header-band { top: 0; height: 170px; }
  .footer-band { bottom: 0; height: 80px; }

  .affiliate {
    position: absolute;
    left: 70px;
    top: 64px;
    display: flex;
    align-items: center;
    gap: 10px;
  }
  .affiliate-mark {
    width: 12px;
    height: 12px;
    border-radius: 50%;
    background: var(--silver);
  }
  .affiliate-name {
    font-family: "Cormorant Garamond", Georgia, serif;
    font-weight: 500;
    font-size: 22px;
    letter-spacing: 3px;
    line-height: 1;
    color: var(--paper);
  }

  .company-name {
    position: absolute;
    right: 48px;
    top: 30px;
    text-align: center;
    font-family: "Cormorant Garamond", Georgia, serif;
    font-weight: 500;
    color: var(--paper);
    margin: 0;
  }
  .company-name .company-main {
    display: block;
    font-size: 25px;
    letter-spacing: 1px;
    line-height: 1.1;
  }
  .company-name .company-sub {
    display: block;
    font-size: 14px;
    letter-spacing: 8px;
    margin-top: 8px;
    margin-right: -8px;
  }

  .contact-line {
    position: absolute;
    left: 0;
    right: 0;
    bottom: 10px;
    display: flex;
    justify-content: center;
    align-items: center;
    gap: 20px;
    font-family: "Montserrat", Arial, sans-serif;
    font-size: 11.5px;
    letter-spacing: 3px;
    color: var(--silver);
  }
  .contact-item {
    display: flex;
    align-items: center;
    gap: 6px;
  }
  .contact-icon {
    width: 13px;
    height: 13px;
    fill: var(--silver);
  }
</style>
</head>
<body>
<main class="letterhead">

  <svg class="header-band" viewBox="0 0 927 170" aria-hidden="true">
    <defs>
      <linearGradient id="headerSilver" x1="0" y1="0" x2="1" y2="0">
        <stop offset="0" stop-color="var(--silver-dark)"/>
        <stop offset="0.25" stop-color="var(--silver-light)"/>
        <stop offset="0.6" stop-color="var(--silver)"/>
        <stop offset="1" stop-color="var(--paper)"/>
      </linearGradient>
    </defs>
    <path d="M0,120 C70,150 170,158 260,142 C380,118 520,98 680,94 C780,92 860,92 927,90 L927,100 C860,104 780,104 680,108 C520,114 380,136 260,158 C170,172 70,160 0,140 Z"
          fill="url(#headerSilver)"/>
    <path d="M0,0 H927 V90 C860,92 780,92 680,94 C520,98 380,118 260,142 C170,158 70,150 0,120 Z"
          fill="var(--black)"/>
  </svg>

  <div class="affiliate">
    <span class="affiliate-mark" aria-hidden="true"></span>
    <span class="affiliate-name">KEYSTONE</span>
  </div>

  <h1 class="company-name">
    <span class="company-main">HARGROVE SUMMIT</span>
    <span class="company-sub">PROPERTIES</span>
  </h1>

  <svg class="footer-band" viewBox="0 0 927 80" aria-hidden="true">
    <defs>
      <linearGradient id="footerSilver" x1="0" y1="0" x2="1" y2="0">
        <stop offset="0" stop-color="var(--silver-dark)"/>
        <stop offset="0.4" stop-color="var(--silver-light)"/>
        <stop offset="0.75" stop-color="var(--silver)"/>
        <stop offset="1" stop-color="var(--silver-dark)"/>
      </linearGradient>
    </defs>
    <path d="M0,24 C250,12 600,10 927,16 L927,40 C600,34 250,34 0,40 Z" fill="url(#footerSilver)"/>
    <path d="M0,36 C250,30 600,30 927,36 L927,80 L0,80 Z" fill="var(--black)"/>
  </svg>

  <footer class="contact-line">
    <span class="contact-item">
      <svg class="contact-icon" viewBox="0 0 24 24" aria-hidden="true">
        <path d="M6.6 10.8a15.1 15.1 0 0 0 6.6 6.6l2.2-2.2a1 1 0 0 1 1-.25 11.4 11.4 0 0 0 3.6.57 1 1 0 0 1 1 1V20a1 1 0 0 1-1 1A17 17 0 0 1 3 4a1 1 0 0 1 1-1h3.5a1 1 0 0 1 1 1c0 1.250.2 2.45.57 3.6a1 1 0 0 1-.25 1z"/>
      </svg>
      281-555-0193
    </span>
    <span class="contact-item">
      <svg class="contact-icon" viewBox="0 0 24 24" aria-hidden="true">
        <circle cx="12" cy="12" r="11"/>
        <path d="M6 8h12v8H6z M6 8l6 5 6-5" fill="none" stroke="#000" stroke-width="1.4"/>
      </svg>
      summit@dalewynnteam.example
    </span>
  </footer>

</main>
</body>
</html>
```